Boutique Wealth management firm needs a new business card design

I want to update my business card design to be more consistent with the look and feel of my website (www.brisvane-wealth.com). I would like to incorporate an ivory parchment background and am open to switching from the current "portrait" layout to a more traditional "landscape" orientation. The final design should convey stability and exclusivity and I want something in PDF format that is ready to send to the printer

Thank you all for taking the time to submit your designs for my project. I've made my decision and picked the design I like best. Thanks again!

```html
<!DOCTYPE html>
<html lang="en">
<head>
<meta charset="utf-8">
<title>Brisvane Wealth Advisory — Business Card</title>
<link rel="stylesheet" href="https://fonts.googleapis.com/css2?family=Tinos:wght@400;700&display=swap">
<style>
  :root {
    --backdrop: #e9e7e4;
    --card: #ffffff;
    --card-shade: #ececec;
    --maroon: #6c2741;
    --ink: #1a1a1a;
    --muted: #3a3a3a;
  }
  * { margin: 0; padding: 0; box-sizing: border-box; }
  html, body {
    width: 1200px; height: 901px; overflow: hidden;
    background: var(--backdrop);
    font-family: "Tinos", "Times New Roman", serif;
  }
  .card {
    position: absolute; left: 150px; top: 193px;
    width: 900px; height: 514px;
    border-radius: 44px; overflow: hidden;
    background: radial-gradient(ellipse at 35% 35%, var(--card) 55%, var(--card-shade) 100%);
    box-shadow: 0 18px 40px rgba(0,0,0,0.18);
  }
  .card-swoosh { position: absolute; inset: 0; width: 100%; height: 100%; }
  .brand {
    position: absolute; left: 78px; top: 84px;
    color: var(--maroon); font-weight: 700; line-height: 1;
  }
  .brand-name { font-size: 76px; letter-spacing: 1px; }
  .brand-tagline { font-size: 31px; margin-top: 4px; padding-left: 10px; }
  .contact-block {
    position: absolute; right: 58px; top: 112px;
    text-align: right; color: var(--muted);
  }
  .person-name { font-size: 26px; color: var(--maroon); line-height: 1.15; }
  .person-title { font-size: 20px; margin-top: 2px; }
  .address { font-size: 17px; line-height: 1.2; margin-top: 38px; }
  .contact-list { list-style: none; margin-top: 22px; font-size: 17px; }
  .contact-list li {
    display: flex; justify-content: flex-end; align-items: center;
    gap: 10px; height: 25px;
  }
  .contact-icon { width: 15px; height: 15px; fill: var(--maroon); flex: none; }
</style>
</head>
<body>
  <article class="card">
    <svg class="card-swoosh" viewBox="0 0 900 514" preserveAspectRatio="none" aria-hidden="true">
      <path d="M0,272 C250,372 550,474 900,508 L900,514 L0,514 Z" fill="var(--maroon)"/>
      <path d="M30,246 C270,346 560,452 900,494 L900,486 C560,444 280,336 30,246 Z" fill="var(--ink)"/>
    </svg>

    <div class="brand">
      <div class="brand-name">BRISVANE</div>
      <div class="brand-tagline">Wealth Advisory</div>
    </div>

    <div class="contact-block">
      <p class="person-name">Daniel Hartwell</p>
      <p class="person-title">President</p>
      <p class="address">210, 12th floor,<br>Harbor Tower Road</p>
      <ul class="contact-list">
        <li>020 555 0148
          <svg class="contact-icon" viewBox="0 0 16 16"><path d="M3 1l3 3-1.5 2a9 9 0 0 0 5.5 5.5L12 10l3 3-2 2C7 15 1 9 1 3z"/></svg>
        </li>
        <li>020 555 0149
          <svg class="contact-icon" viewBox="0 0 16 16"><path d="M4 0h8v16H4zM5.5 2v10h5V2zM7 13.2h2v1.4H7z" fill-rule="evenodd"/></svg>
        </li>
        <li>020 555 0150
          <svg class="contact-icon" viewBox="0 0 16 16"><path d="M4 1h7v4H4zM1 6h14v9H1zM4 9v3h8V9z" fill-rule="evenodd"/></svg>
        </li>
        <li>info@brisvane.com
          <svg class="contact-icon" viewBox="0 0 16 16"><path d="M1 3h14v10H1zM2.5 4.5L8 9l5.5-4.5z" fill-rule="evenodd"/></svg>
        </li>
        <li>www.brisvane-wealth.com
          <svg class="contact-icon" viewBox="0 0 16 16"><path d="M8 1a7 7 0 1 0 0 14A7 7 0 0 0 8 1zm0 1.5c1 1.3 1.6 3 1.7 4.8H6.3C6.4 5.5 7 3.8 8 2.5zM2.6 7.3h2.3c.1-1.6.5-3 1.1-4.3a5.6 5.6 0 0 0-3.4 4.3zm0 1.4a5.6 5.6 0 0 0 3.4 4.3c-.6-1.3-1-2.7-1.1-4.3zm3.7 0h3.4c-.1 1.8-.7 3.5-1.7 4.8-1-1.3-1.6-3-1.7-4.8zm4.8 0c-.1 1.6-.5 3-1.1 4.3a5.6 5.6 0 0 0 3.4-4.3zm0-1.4h2.3A5.6 5.6 0 0 0 10 3c.6 1.3 1 2.7 1.1 4.3z" fill-rule="evenodd"/></svg>
        </li>
      </ul>
    </div>
  </article>
</body>
</html>
```